Gains Beyond the Lantern Gate - book cover design

I need a cover designed for a new book (paperback and eBook).
The title is: “Gains Beyond the Lantern Gate” with the subtitle: “The only book you need to start investing profitably in Chinese stocks”. It is from the first time author :“Teemu Harkala“.
The following text should also be visible in the front cover: “From the founder of OrientWagerly.com” or "Founder of OrientWagerly.com".
The publisher’s logo, should also be visible somewhere on the cover (front, back or spine). The logo, along with source files are here: http://filevault.example/k7Tq2Lp
The book/paperback cover dimensions are: 5.06 x 7.81 inches (12.9 x 19.8 centimeters). Here are the book-cover templates recommended by Bookdale for a book of this size:
http://filevault.example/z3Wm9Xa (.indd)
http://filevault.example/r8Nd4Fu (.pdf)
Below is a description of the book. I don't have a specific idea or vision in mind for the cover. I'd like to see what designs and ideas ArtHuddle designers come up with.
Color red is usually associated with China, but I don’t want the book to be red. Instead the background color could be one of the publisher’s brand colors (#88C198, #017487). However I’ll leave you the designers freedom to propose any colors and combinations.
This is not an entry level book, but a very advanced level investment strategy book for international investors. It explains with concrete examples how non-Chinese citizens can best benefit from China’s economic miracle by picking the best Chinese growth stocks from New York, Hong Kong and Singapore stock exchanges.
The book cover should not have dollar signs promising easy and fast money (because easy and fast money doesn’t exist). What the book promises is a very advanced level China investing strategy, which will considerably improve international investors’ odds for big profits in the longer term.
The big investment themes in the book are China’s consumer sector and service industries.
The book cover should have some kind of reference/association to Investing and China.
The design needs to work and be effective at both a large book cover size and a small thumbnail-sized image - the way that many people browse book covers on Bookdale and other websites. Therefore, a design that relies on really small details probably won't translate at the smaller image sizes that book covers are displayed online.
Target Market(s)
International investors (~50% from western countries, 30% from Singapore/Hong Kong, Malaysia)
Industry/Entity Type
Investment
Font styles to use
Other font styles liked:
- EB Garamond, Grimson text or some other beautiful book font
Look and feel
Each slider illustrates characteristics of the customer's brand and the style your logo design should communicate.

```html
<!DOCTYPE html>
<html lang="en">
<head>
<meta charset="utf-8">
<title>Gains Beyond the Lantern Gate — Front Cover</title>
<link rel="stylesheet" href="https://fonts.googleapis.com/css2?family=Cinzel:wght@400;500;600&family=Marcellus&display=swap">
<style>
  :root {
    --page-bg: #ffffff;
    --cover-bg: #ffffff;
    --ink-navy: #1f2d3d;
    --title-teal: #137f86;
    --sky: #f1f1ee;
    --haze: #d9d6cf;
    --street: #c9bcaa;
    --stone: #6e6459;
    --shadow-wall: #3b302b;
    --lantern: #9a3a33;
  }
  * { margin: 0; padding: 0; box-sizing: border-box; }
  html, body {
    width: 1200px;
    height: 1200px;
    overflow: hidden;
    background: var(--page-bg);
  }
  .stage {
    width: 1200px;
    height: 1200px;
    display: flex;
    align-items: center;
    justify-content: center;
  }
  .cover {
    position: relative;
    width: 700px;
    height: 1080px;
    background: var(--cover-bg);
    overflow: hidden;
    box-shadow: 0 0 0 1px #e6e6e6;
  }
  .founder-note {
    position: absolute;
    top: 44px;
    left: 0;
    right: 0;
    text-align: center;
    font-family: "Cinzel", serif;
    font-weight: 500;
    font-size: 17px;
    letter-spacing: 1.5px;
    color: var(--ink-navy);
  }
  .author {
    position: absolute;
    top: 88px;
    left: 0;
    right: 0;
    text-align: center;
    font-family: "Cinzel", serif;
    font-weight: 500;
    font-size: 40px;
    letter-spacing: 3px;
    color: var(--ink-navy);
  }
  .title {
    position: absolute;
    top: 182px;
    left: 0;
    right: 0;
    text-align: center;
    font-family: "Marcellus", serif;
    font-weight: 400;
    color: var(--title-teal);
    line-height: 0.98;
    text-transform: uppercase;
  }
  .title .line { display: block; font-size: 76px; letter-spacing: 1px; }
  .title .line--big { font-size: 118px; letter-spacing: 2px; }
  .subtitle {
    position: absolute;
    top: 458px;
    left: 0;
    right: 0;
    z-index: 2;
    text-align: center;
    font-family: "Cinzel", serif;
    font-weight: 600;
    font-size: 24px;
    line-height: 1.12;
    letter-spacing: 0.5px;
    color: var(--ink-navy);
    text-transform: uppercase;
  }
  .street-photo {
    position: absolute;
    left: 0;
    right: 0;
    top: 430px;
    bottom: 0;
    background:
      linear-gradient(to bottom, var(--cover-bg) 0%, rgba(255,255,255,0.85) 16%, rgba(255,255,255,0) 36%),
      linear-gradient(to right, var(--shadow-wall) 0%, var(--lantern) 14%, var(--stone) 26%, var(--haze) 42%, var(--sky) 50%, var(--haze) 60%, var(--stone) 74%, var(--lantern) 86%, var(--shadow-wall) 100%);
  }
  .street-photo::after {
    content: "";
    position: absolute;
    left: 0;
    right: 0;
    bottom: 0;
    height: 38%;
    background: linear-gradient(to bottom, rgba(201,188,170,0) 0%, var(--street) 55%, #d8cdbf 100%);
  }
  .publisher {
    position: absolute;
    bottom: 30px;
    left: 0;
    right: 0;
    z-index: 2;
    display: flex;
    align-items: center;
    justify-content: center;
    gap: 10px;
    font-family: "Cinzel", serif;
    font-weight: 600;
    font-size: 18px;
    letter-spacing: 2px;
    color: var(--ink-navy);
  }
  .publisher-dot {
    width: 14px;
    height: 14px;
    border-radius: 50%;
    background: var(--ink-navy);
  }
</style>
</head>
<body>
  <main class="stage">
    <article class="cover">
      <div class="street-photo" role="img" aria-label="Photograph of a busy old Chinese street with traditional shopfronts, red lanterns, cyclists and pedestrians leading toward a tall pagoda gate tower"></div>
      <p class="founder-note">From the founder of OrientWagerly.com</p>
      <p class="author">Teemu Harkala</p>
      <h1 class="title">
        <span class="line">Gains Beyond</span>
        <span class="line">The Lantern</span>
        <span class="line line--big">Gate</span>
      </h1>
      <p class="subtitle">The only book you need<br>to start investing profitably<br>in Chinese stocks</p>
      <p class="publisher"><span class="publisher-dot"></span>Lanternfold Press</p>
    </article>
  </main>
</body>
</html>
```